Online Trading Web-Design

Web design is required for a new startup that specialises in online trading between buyers and sellers of fashion apparel. The company is called: Blue Harbor Commons (bhc)

Website needs to be clean and css friendly. we like the idea of having a largish "banner" on the homepage which we can rotate using HTML5. examples of the banners are: http://au.vextrano.com/ ; http://www.plorvak.com.au/

the logo has been established already, please limit designs around the colors already established (see uploaded logo).
Updates

Hi, a few clarifications:

1. although the website deals in online trading for clothes etc. the main focus of the website needs to be about highlighting trading between buyers (clothing stores) and sellers (clothing brands). so the website wont be directly selling items of clothes etc.

Industry/Entity Type

Fashion

```html
<!DOCTYPE html>
<html lang="en">
<head>
<meta charset="utf-8">
<title>Blue Harbor Commons</title>
<link href="https://fonts.googleapis.com/css2?family=Arimo:wght@400;700&display=swap" rel="stylesheet">
<style>
:root{
  --teal:#5bc3cb;
  --aqua:#a6e6ea;
  --aqua-light:#d3f3f5;
  --text:#555;
  --dark:#333;
  --line:#d6d6d6;
  --panel:#ececec;
  --slate:#4e4e4e;
}
*{box-sizing:border-box;margin:0;padding:0}
html,body{width:1104px;height:1200px;overflow:hidden;background:#fff}
body{position:relative;font-family:"Arimo",Arial,sans-serif;color:var(--text)}
.topbar{position:absolute;left:0;top:0;width:1104px;height:8px;background:var(--aqua)}
.brand{position:absolute;left:86px;top:30px}
.brand-mark{display:flex;align-items:center;gap:8px}
.brand-square{width:26px;height:26px;background:var(--aqua)}
.brand-name{font-size:44px;font-weight:700;color:var(--teal);line-height:1}
.brand-sub{font-size:15px;color:#8c8c8c;margin-top:30px}
.search{position:absolute;left:807px;top:91px;width:213px;height:31px;border:1px solid #cfcfcf;font-size:11px;color:#888;padding:9px 11px}
.search svg{position:absolute;right:9px;top:7px}
.nav{position:absolute;left:83px;top:143px;width:939px;height:49px;display:flex;background:linear-gradient(#d8f5f7,#a9e3e8);border-top:1px solid #bfe9ec;border-bottom:1px solid #bfe9ec}
.nav a{display:flex;align-items:center;justify-content:center;font-size:13px;font-weight:700;color:#3d3d3d;text-decoration:none;border-right:1px solid #8fd3d9}
.nav a:last-child{border-right:0}
.nav a.active{background:linear-gradient(#b9ecef,#7fd2d9)}
.banner{position:absolute;left:83px;top:200px;width:939px;height:297px;border:5px solid #d9d9d9;background:linear-gradient(90deg,#3a3a3a,#606060 60%,#4a4a4a);overflow:hidden}
.banner-photo{position:absolute;right:60px;top:0;width:220px;height:287px;background:linear-gradient(160deg,#7a5a48,#5a3c3c 40%,#2f4650 75%,#484848)}
.banner-offer{position:absolute;left:48px;top:26px;width:234px;height:233px;background:#262626;border-radius:3px;color:#fff;text-align:center}
.banner-offer h2{font-size:35px;margin-top:36px}
.banner-offer p{font-size:23px;font-weight:700;margin-top:10px}
.banner-offer strong{display:block;font-size:70px;margin-top:6px;letter-spacing:-2px}
.banner-label{position:absolute;left:282px;top:48px;width:231px;height:193px;background:linear-gradient(#6f6f6f,#9b9b9b);display:flex;align-items:center;justify-content:center;font-size:14px;color:#222;letter-spacing:1px}
.slide-arrow{position:absolute;top:317px;width:24px;height:60px;background:#fff;display:flex;align-items:center;justify-content:center}
.slide-arrow.left{left:83px;border-radius:0 30px 30px 0}
.slide-arrow.right{left:998px;border-radius:30px 0 0 30px}
.sidebar{position:absolute;left:83px;top:510px;width:244px;height:515px;border:1px solid var(--line);padding:5px}
.side-head{background:var(--panel);height:34px;font-size:16px;font-weight:700;color:#444;padding:9px 9px;margin-bottom:6px}
.side-list{list-style:none;padding:7px 0 6px 14px}
.side-list li{font-size:12.5px;color:#555;height:23.2px}
.side-list li::before{content:"\203A\203A";margin-right:12px;color:#666}
.main{position:absolute;left:353px;top:518px;width:669px}
.main h1{font-size:20px;color:var(--teal);font-weight:700}
.main .intro{font-size:12.5px;line-height:21.3px;margin-top:16px;color:#555}
.cards{position:absolute;left:353px;top:666px;width:669px;display:flex;justify-content:space-between}
.card{width:214px;height:281px;border:1px solid var(--line);padding:0 5px}
.card-head{display:flex;justify-content:space-between;align-items:center;height:32px;padding:0 7px;font-size:17px;font-weight:700;color:var(--teal)}
.card-body{background:#f5f5f5;height:240px;padding:7px 7px}
.card-photo{height:97px}
.card-brands{height:97px;background:#fff;display:flex;flex-wrap:wrap;align-content:center;justify-content:space-around;gap:12px 6px;font-size:11px;font-weight:700;color:#666;padding:6px}
.card-link{font-size:12.5px;color:var(--teal);line-height:17px;margin-top:13px}
.card-text{font-size:11px;line-height:17px;color:#444;margin-top:7px}
.card-date{font-size:11.5px;color:#222;margin-top:5px}
.newsletter{position:absolute;left:353px;top:958px;width:669px;height:67px;border:1px solid var(--line);padding:5px}
.newsletter-inner{background:var(--slate);height:100%;display:flex;align-items:center;padding:0 14px 0 32px}
.newsletter h3{font-size:23px;color:#d0d0d0;font-weight:700;width:266px}
.newsletter .field{width:272px;height:31px;background:#fff;font-size:11px;color:#888;padding:10px 11px}
.newsletter .submit{margin-left:8px;width:92px;height:31px;background:linear-gradient(#aaa,#777);color:#fff;font-size:16px;font-weight:700;display:flex;align-items:center;justify-content:center}
.partners{position:absolute;left:83px;top:1050px;width:939px;height:70px;border-top:1px solid var(--line);border-bottom:1px solid var(--line);display:flex;align-items:center;justify-content:space-around;padding:0 24px;font-size:12px;font-weight:700;color:#777}
.partner-badge{width:30px;height:30px;border-radius:50%;background:#c9c9c9}
.footer-nav{position:absolute;left:83px;top:1143px;font-size:12px;color:#555}
.footer-nav span{margin:0 8px;color:#888}
.copyright{position:absolute;left:83px;top:1173px;font-size:12px;color:#555}
.social{position:absolute;left:967px;top:1155px;display:flex;gap:10px}
.social i{width:25px;height:25px;border-radius:50%;background:#aaa;display:block}
</style>
</head>
<body>
<div class="topbar"></div>

<div class="brand">
  <div class="brand-mark"><span class="brand-square"></span><span class="brand-name">bhc</span></div>
  <div class="brand-sub">Blue Harbor Commons</div>
</div>

<div class="search">Search
  <svg width="16" height="16" viewBox="0 0 16 16"><circle cx="6" cy="6" r="4.5" fill="#222"/><line x1="9" y1="9" x2="14" y2="14" stroke="#222" stroke-width="3" stroke-linecap="round"/></svg>
</div>

<nav class="nav">
  <a class="active" style="width:120px">Home</a>
  <a style="width:123px">About us</a>
  <a style="width:108px">Servies</a>
  <a style="width:119px">Products</a>
  <a style="width:111px">Brands</a>
  <a style="width:106px">Stores</a>
  <a style="width:108px">Sellers</a>
  <a style="width:144px">Contact us</a>
</nav>

<section class="banner">
  <div class="banner-photo" role="img" aria-label="Young man in a plaid flannel shirt"></div>
  <div class="banner-offer"><h2>New Styles</h2><p>Save upto</p><strong>40%</strong></div>
  <div class="banner-label">VARNO LISETTI</div>
</section>
<div class="slide-arrow left"><svg width="10" height="14" viewBox="0 0 10 14"><path d="M8 2 3 7l5 5" fill="none" stroke="#222" stroke-width="2.5"/></svg></div>
<div class="slide-arrow right"><svg width="10" height="14" viewBox="0 0 10 14"><path d="M2 2l5 5-5 5" fill="none" stroke="#222" stroke-width="2.5"/></svg></div>

<aside class="sidebar">
  <div class="side-head">Men's Clothing</div>
  <ul class="side-list">
    <li>Men's Jackets &amp; Coats</li><li>Men's Shirts</li><li>Men's Pants</li>
    <li>Men's Sweatshirts &amp; Sweaters</li><li>Men's Suits &amp; Sport Coats</li>
    <li>Men's Accessories</li><li>Men's Underwear &amp; Base Layer</li><li>Men's Socks</li>
    <li>Men's Shorts</li><li>Men's Vests</li><li>Men's Sleepwear &amp; Robes</li>
    <li>Men's Overalls &amp; Coveralls</li><li>Men's Swimwear</li>
  </ul>
  <div class="side-head">Women's Clothing</div>
  <div class="side-head">Kids' Clothing</div>
  <div class="side-head">Brands</div>
  <div class="side-head">Popular Categories</div>
</aside>

<main class="main">
  <h1>Welcome to our site</h1>
  <p class="intro">Phasellus non erat at ligula imperdiet luctus. Donec convallis urna ac tellus sollicitudin lacinia. Lorem ipsum dolor sit amet, consectetur adipiscing elit. Donec a quam magna, vel scelerisque ligula. Nulla eu orci quis nisi tincidunt pellentesque tincidunt id dolor. Nulla facilisi. Phasellus ullamcorper arcu et magna sodales vel dignissim urna tincidunt. Duis condimentum, mauris ut euismod ultrices, libero ligula luctus risus, eget congue neque lacus at justo.</p>
</main>

<div class="cards">
  <article class="card">
    <div class="card-head">Latest Blog<svg width="9" height="12" viewBox="0 0 9 12"><path d="M2 1l5 5-5 5" fill="none" stroke="#777" stroke-width="2"/></svg></div>
    <div class="card-body">
      <div class="card-photo" role="img" aria-label="Man wearing a red plaid shirt" style="background:linear-gradient(90deg,#b9a99a,#7a4d52 40%,#6b3f46 60%,#c2b5a8)"></div>
      <p class="card-link">Cras libero diam, dapibus vitae facilisis at, blandit nec velit.</p>
      <p class="card-text">Pellacinia thika accumsan, enim dui lobortis odio, faucibus congue mi mauris vitae dui.</p>
      <p class="card-date">April - 9 - 2013</p>
    </div>
  </article>
  <article class="card">
    <div class="card-head">Top Brands<svg width="9" height="12" viewBox="0 0 9 12"><path d="M2 1l5 5-5 5" fill="none" stroke="#777" stroke-width="2"/></svg></div>
    <div class="card-body">
      <div class="card-brands"><span>Corvo</span><span>Tessaro</span><span>Ridgeline</span><span>Meridian Wear</span><span class="partner-badge" style="width:22px;height:22px"></span></div>
      <p class="card-link">Cras libero diam, dapibus vitae facilisis at, blandit nec velit.</p>
      <p class="card-text">Pellacinia thika accumsan, enim dui lobortis odio, faucibus congue mi mauris vitae dui.</p>
      <p class="card-date">April - 9 - 2013</p>
    </div>
  </article>
  <article class="card">
    <div class="card-head">Top Sellers<svg width="9" height="12" viewBox="0 0 9 12"><path d="M2 1l5 5-5 5" fill="none" stroke="#777" stroke-width="2"/></svg></div>
    <div class="card-body">
      <div class="card-photo" role="img" aria-label="Printed graphic t-shirt close-up" style="background:linear-gradient(135deg,#5a5a55,#9d9a90 50%,#3e3d3a)"></div>
      <p class="card-link">Cras libero diam, dapibus vitae facilisis at, blandit nec velit.</p>
      <p class="card-text">Pellacinia thika accumsan, enim dui lobortis odio, faucibus congue mi mauris vitae dui.</p>
      <p class="card-date">April - 9 - 2013</p>
    </div>
  </article>
</div>

<section class="newsletter">
  <div class="newsletter-inner">
    <h3>Newsletter Subscribe</h3>
    <div class="field">Search</div>
    <div class="submit">SUBMIT</div>
  </div>
</section>

<div class="partners">
  <span>Dunmore</span><span>Orchard Loom</span><span>Hale &amp; Pike</span>
  <span>Meridian Wear</span><span class="partner-badge"></span>
  <span>Corvo</span><span>Tessaro</span><span>Ridgeline</span>
  <span>Harlow</span><span>Northfield Apparel</span>
</div>

<nav class="footer-nav">Home<span>|</span>About us<span>|</span>Servies<span>|</span>Products<span>|</span>Brands<span>|</span>Stores<span>|</span>Sellers<span>|</span>Contact us</nav>
<p class="copyright">Copyright &copy; 2013 &nbsp; www.bhc.com &nbsp; All rioghts reserved.</p>
<div class="social"><i></i><i></i></div>
</body>
</html>
```